Bikes for Dreams - Website Redesign

Create a professional website for a nonprofit; BikesforDreams.org
Please see bikesforelders.org and www.pedalsforhopes.org for the concept I am after.
The webpage should have a fun feel and should match the style of the company at www.pedalsforhopes.org. The pages to include are 'Home', 'About us' and 'Get Started'
Thank you and good luck!

```html
<!DOCTYPE html>
<html lang="en">
<head>
<meta charset="utf-8">
<title>Bikes for Dreams Foundation</title>
<link rel="stylesheet" href="https://fonts.googleapis.com/css2?family=Open+Sans:wght@400;600;700;800&family=Exo+2:wght@600;700&display=swap">
<style>
:root{
  --navy:#0b3a78;
  --blue:#0d4f9e;
  --deep:#072a57;
  --red:#d61f26;
  --grey:#e7e8ea;
  --light:#f4f5f6;
  --text:#333;
  --muted:#666;
  --white:#fff;
}
*{box-sizing:border-box;margin:0;padding:0}
html,body{width:1200px;height:2368px;overflow:hidden}
body{font-family:"Open Sans",Arial,sans-serif;color:var(--text);background:var(--white);position:relative}
.header{position:absolute;left:0;top:0;width:1200px;height:130px}
.brand{position:absolute;left:0;top:0;width:560px;height:130px;background:var(--navy);padding:26px 0 0 40px;color:var(--white);white-space:nowrap}
.brand-name{font-weight:800;font-size:40px;line-height:44px;letter-spacing:1px}
.brand-sub{font-weight:400;font-size:26px;line-height:34px;letter-spacing:1px}
.topbar{position:absolute;left:560px;top:0;width:640px;height:40px;background:var(--deep);display:flex;justify-content:flex-end;align-items:center;gap:26px;padding-right:30px;font-size:15px;font-weight:600;color:var(--white)}
.topbar .donate{font-weight:800}
.contactbar{position:absolute;left:560px;top:40px;width:640px;height:90px;background:var(--red);display:flex;align-items:center;gap:24px;padding-left:40px;color:var(--white);font-size:15px;white-space:nowrap}
.contactbar .item{display:flex;align-items:center;gap:8px}
.socials{display:flex;gap:8px;margin-left:auto;margin-right:30px}
.socials span{width:22px;height:22px;border-radius:50%;background:var(--white);opacity:.9}
.nav{position:absolute;left:0;top:130px;width:1200px;height:56px;background:var(--light);border-bottom:3px solid var(--navy);display:flex;align-items:center;padding-left:110px;gap:8px;white-space:nowrap}
.nav a{font-size:14px;font-weight:600;color:var(--navy);text-decoration:none;padding:8px 22px}
.nav a.active{background:var(--white);border-bottom:3px solid var(--red)}
.hero{position:absolute;left:0;top:189px;width:1200px;height:600px;background:linear-gradient(100deg,#3a3a3f 0%,#6e6a68 35%,#9aa3ad 65%,#c4ccd4 100%)}
.hero-title{position:absolute;left:640px;top:280px;font-family:"Exo 2","Open Sans",sans-serif;font-weight:700;font-size:46px;line-height:56px;color:var(--white);white-space:nowrap}
.hero-sub{position:absolute;left:640px;top:342px;font-family:"Exo 2","Open Sans",sans-serif;font-size:26px;line-height:34px;color:#dfe6ee;font-weight:600;white-space:nowrap}
.form{position:absolute;left:905px;top:400px;width:275px;height:660px;background:var(--navy);padding:0 18px}
.form-head{margin:14px -8px 0;background:var(--white);color:var(--navy);font-family:"Exo 2","Open Sans",sans-serif;font-weight:700;font-size:28px;padding:8px 10px;text-align:center;white-space:nowrap}
.form h4{color:var(--white);font-size:13px;font-weight:700;margin:16px 0 8px;text-transform:uppercase;white-space:nowrap}
.form .field{height:26px;background:var(--white);margin-bottom:9px;font-size:11px;color:#888;padding:5px 8px}
.form .submit{background:var(--red);color:var(--white);font-size:13px;font-weight:700;width:160px;padding:8px 0;text-align:center;margin-top:8px;white-space:nowrap}
.intro{position:absolute;left:55px;top:815px;width:820px}
.intro h1{font-size:27px;font-weight:800;color:var(--navy)}
.intro h2{font-size:20px;color:var(--blue);font-weight:600;margin:4px 0 14px}
.intro p{font-size:14px;line-height:22px;color:var(--muted)}
.intro ul{margin:14px 0 0 20px;font-size:14px;line-height:22px;color:var(--muted)}
.intro b{color:var(--text)}
.btn{display:inline-block;background:var(--navy);color:var(--white);font-size:14px;font-weight:700;padding:10px 20px;margin-top:18px}
.services{position:absolute;left:0;top:1220px;width:1200px;height:410px;background:var(--grey);display:flex;gap:26px;padding:40px 55px}
.card{flex:1;background:var(--white);text-align:center;padding:20px 18px}
.icon{width:96px;height:96px;margin:0 auto}
.card h3{font-size:18px;font-weight:800;color:var(--navy);margin:14px 0 10px;line-height:22px;text-transform:uppercase}
.card p{font-size:12px;line-height:18px;color:var(--muted)}
.card .more{display:inline-block;background:#2b2b2b;color:var(--white);font-size:11px;font-weight:700;padding:8px 22px;margin-top:14px}
.mission{position:absolute;left:0;top:1660px;width:1200px;text-align:center;padding:0 110px}
.mission h2{font-size:32px;color:var(--navy);font-weight:800}
.mission .bar{width:90px;height:3px;background:var(--red);margin:10px auto 18px}
.mission p{font-size:14px;line-height:22px;color:var(--muted)}
.newsletter{position:absolute;left:0;top:1900px;width:1200px;height:468px;background:var(--blue);text-align:center;color:var(--white)}
.newsletter h2{font-size:38px;font-weight:700;margin-top:70px}
.newsletter p{font-size:17px;color:#d6e2f2;margin-top:6px}
.subscribe{display:flex;justify-content:center;margin-top:24px}
.subscribe .input{width:370px;height:46px;background:var(--white);border-radius:23px 0 0 23px;color:#999;text-align:left;padding:12px 22px;font-size:14px}
.subscribe .send{width:60px;height:46px;background:var(--deep);border-radius:0 23px 23px 0;display:flex;align-items:center;justify-content:center}
.foot-social{display:flex;justify-content:center;gap:14px;margin-top:24px}
.foot-social span{width:28px;height:28px;border-radius:50%;background:var(--white)}
.footer-links{position:absolute;left:0;bottom:0;width:1200px;height:70px;border-top:1px solid rgba(255,255,255,.3);display:flex;justify-content:center;align-items:center;gap:22px;font-size:14px}
</style>
</head>
<body>
<header class="header">
  <div class="brand"><div class="brand-name">BIKES FOR DREAMS</div><div class="brand-sub">FOUNDATION</div></div>
  <div class="topbar"><span>LOGIN</span><span>REGISTER</span><span class="donate">DONATE NOW</span></div>
  <div class="contactbar">
    <div class="item"><svg width="16" height="16" viewBox="0 0 16 16"><path d="M3 1h3l1 4-2 1a9 9 0 0 0 5 5l1-2 4 1v3a2 2 0 0 1-2 2A12 12 0 0 1 1 3a2 2 0 0 1 2-2z" fill="#fff"/></svg>1-800-555-0142</div>
    <div class="item"><svg width="18" height="14" viewBox="0 0 18 14"><rect x="1" y="1" width="16" height="12" fill="none" stroke="#fff" stroke-width="1.6"/><path d="M1 1l8 7 8-7" fill="none" stroke="#fff" stroke-width="1.6"/></svg>info@bikesfordreams.org</div>
    <div class="socials"><span></span><span></span><span></span><span></span><span></span></div>
  </div>
</header>
<nav class="nav"><a class="active">HOME</a><a>ABOUT US</a><a>GET STARTED</a><a>WHY DONATE YOUR CAR</a><a>CONTACT US</a></nav>

<div class="hero" role="img" aria-label="Photo of a smiling woman seated behind the wheel of a car"></div>
<div class="hero-title">Donate Car to Charity!</div>
<div class="hero-sub">Your car can make a difference!</div>

<aside class="form">
  <div class="form-head">Donate Online!</div>
  <h4>Contact Information</h4>
  <div class="field">First Name</div><div class="field">Last Name</div><div class="field">Email</div><div class="field">Confirm Email</div><div class="field">Day Phone</div><div class="field">Zip Code</div><div class="field">Vehicle Location</div>
  <h4>Vehicle Donation Information</h4>
  <div class="field">Make of Vehicle</div><div class="field">Model of Vehicle</div><div class="field">Year of Vehicle</div>
  <div class="submit">SUBMIT APPLICATION</div>
</aside>

<section class="intro">
  <h1>BIKES FOR DREAMS FOUNDATION</h1>
  <h2>Lorem ipsum dolor sit amet</h2>
  <p>Lorem ipsum dolor sit amet, consectetur adipiscing elit. Vivamus sagittis non posuere felis sollicitudin volutpat. Sed sodales sollicitudin mauris. Curabitur pellentesque sagittis mi, vitae tempus eros.</p>
  <ul>
    <li><b>Free Local Towing:</b> Running or not, Any Condition &amp; Pickup Anywhere.</li>
    <li><b>Fast Pickup:</b> Same Day to 24 Hours.</li>
    <li><b>Income Tax Deduction:</b> We issue you an IRS tax receipt &amp; offer the largest resale network to get you the highest tax write-off possible.</li>
    <li><b>No Paperwork Hassles:</b> We take any car and handle everything: DMV, Smog, &amp; IRS paperwork.</li>
    <li><b>Car donations help fund programs:</b> And benefit Bikes for Dreams Foundation, an IRS 501(c)3 nonprofit organization.</li>
  </ul>
  <div class="btn">Donate Now</div>
</section>

<section class="services">
  <div class="card">
    <svg class="icon" viewBox="0 0 96 96"><circle cx="48" cy="48" r="46" fill="var(--navy)"/><circle cx="48" cy="48" r="38" fill="none" stroke="#fff" stroke-width="2"/><rect x="24" y="44" width="30" height="14" fill="#fff"/><path d="M54 58V46h10l8 8v4z" fill="#fff"/><circle cx="34" cy="62" r="5" fill="#fff"/><circle cx="62" cy="62" r="5" fill="#fff"/></svg>
    <h3>Towing<br>is Free</h3><p>Lorem ipsum dolor sit amet, sed sodales mauris curabitur tempus eros vitae felis sollicitudin.</p><div class="more">VIEW MORE</div>
  </div>
  <div class="card">
    <svg class="icon" viewBox="0 0 96 96"><circle cx="48" cy="48" r="46" fill="var(--navy)"/><circle cx="48" cy="48" r="22" fill="none" stroke="#fff" stroke-width="3"/><ellipse cx="48" cy="48" rx="10" ry="22" fill="none" stroke="#fff" stroke-width="2"/><path d="M26 48h44M30 38h36M30 58h36" stroke="#fff" stroke-width="2"/></svg>
    <h3>Donations<br>Accepted Nationwide</h3><p>Lorem ipsum dolor sit amet, vivamus sagittis non posuere felis volutpat sed sodales mauris.</p><div class="more">VIEW MORE</div>
  </div>
  <div class="card">
    <svg class="icon" viewBox="0 0 96 96"><circle cx="48" cy="48" r="46" fill="var(--navy)"/><path d="M24 56v-8l6-10h36l6 10v8z" fill="#fff"/><circle cx="34" cy="58" r="5" fill="var(--navy)" stroke="#fff" stroke-width="2"/><circle cx="62" cy="58" r="5" fill="var(--navy)" stroke="#fff" stroke-width="2"/></svg>
    <h3>All Vechile<br>Types Welcome</h3><p>Interdum sed, quam accumsan mattis porttitor, pellentesque sagittis mi vitae tempus.</p><div class="more">VIEW MORE</div>
  </div>
  <div class="card">
    <svg class="icon" viewBox="0 0 96 96"><circle cx="48" cy="48" r="46" fill="var(--navy)"/><circle cx="48" cy="48" r="22" fill="none" stroke="#fff" stroke-width="3"/><path d="M37 48l8 8 14-15" fill="none" stroke="#fff" stroke-width="4"/></svg>
    <h3>Tax<br>Deductible</h3><p>Lorem ipsum dolor sit amet, curabitur pellentesque sagittis mi, vitae tempus eros felis.</p><div class="more">VIEW MORE</div>
  </div>
</section>

<section class="mission">
  <h2>OUR MISSION</h2><div class="bar"></div>
  <p>Lorem ipsum dolor sit amet, consectetur adipiscing elit. Nulla elementum enim at porttitor ullamcorper. Proin convallis pellentesque tristique. Suspendisse enim neque, lobortis sit amet lacus id, commodo volutpat odio. Pellentesque eget lacus vitae sem sagittis eleifend eget in est. Nullam imperdiet eros id quam aliquet tempor eget rhoncus at. Duis eleifend mauris nulla, in malesuada eros consectetur id. Aliquam quis lacus sodales, egestas massa eget, facilisis velit. Nam finibus, leo tincidunt sagittis placerat, odio eros congue ipsum, a lacinia lectus magna non lectus. Maecenas felis lacus, lacinia in dolor eget, gravida fringilla magna. Sed pharetra rutrum rhoncus. Integer blandit porta condimentum. Sed tincidunt ipsum a metus aliquam.</p>
</section>

<section class="newsletter">
  <h2>STAY TUNED!</h2>
  <p>We'll do our best to deliver valuable updates and lots of great resources without invading your mailbox.</p>
  <div class="subscribe"><div class="input">your email address</div><div class="send"><svg width="24" height="22" viewBox="0 0 24 22"><path d="M1 1l22 10L1 21l4-10z" fill="#fff"/></svg></div></div>
  <div class="foot-social"><span></span><span></span><span></span><span></span><span></span></div>
  <div class="footer-links"><span>Home</span><span>/</span><span>About us</span><span>/</span><span>Get Started</span><span>/</span><span>Why donate your car</span><span>/</span><span>Contact us</span></div>
</section>
</body>
</html>
```